PPT template for BLM. Whiskey, wine, food, drink and music. Moments in time

Velvet Crane and Cellars. Liquor, food, music. Need slides for BLM, Liquor, food and music.

Think whiskey distillery meets music studio.

Its about moments in time with the people we love. Music, food and drink all play apart in the times we remember.

Target Market(s)

Investors

Industry/Entity Type

Entertainment

Colors

Designer to choose colors to be used in the design.

Requirements
Must have
• Utilize the logo or image without text in all slides.
Nice to have
• blank template pages with logo or just image. multiple versions I can utilize. Logo and image as backgrounds, logo in corner and so on. Logo in many colors, rainbow, nautilus shell. Golden ratio....
Should not have
• Do not need close ups of food. its about people and experiences and food is part of this. Think tables, parties, events, chocolate fountains, and so on

```html
<!DOCTYPE html>
<html lang="en">
<head>
<meta charset="utf-8">
<title>Velvet Crane Slide Deck Template</title>
<link href="https://fonts.googleapis.com/css2?family=Montserrat:wght@400;600;700;800&family=Open+Sans:wght@400;600&display=swap" rel="stylesheet">
<style>
:root{
  --navy:#26297f;
  --blue:#3a3fae;
  --grey:#e7e7ee;
  --mid:#b9bacb;
  --text:#6b6c80;
  --white:#ffffff;
  --page:#f3f3f6;
}
*{box-sizing:border-box;margin:0;padding:0}
html,body{width:1200px;height:2916px;overflow:hidden;background:var(--page)}
body{font-family:"Open Sans",sans-serif;color:var(--text)}
.deck{display:grid;grid-template-columns:repeat(3,388px);grid-auto-rows:212px;gap:12px;padding:6px}
.slide{position:relative;background:var(--white);overflow:hidden;box-shadow:0 0 0 1px #dcdce4}
.slide.dark{background:var(--navy)}
.abs{position:absolute}
.h{font-family:"Montserrat",sans-serif;font-weight:700;font-size:11px;color:var(--navy);line-height:1.2}
.h.w{color:var(--white)}
.p{font-size:6px;line-height:1.5;color:var(--text)}
.p.w{color:#d9dbf5}
.photo{position:absolute}
.ph-night{background:linear-gradient(135deg,#1c1f5e,#4b4fa8 55%,#8f8ec4)}
.ph-warm{background:linear-gradient(135deg,#4a2a1c,#b26b2c 55%,#e9b46a)}
.ph-neon{background:linear-gradient(135deg,#3b0d12,#b4202b 50%,#f08a3a)}
.ph-grey{background:linear-gradient(135deg,#8d8e9c,#d3d4dc)}
.ph-bar{background:linear-gradient(135deg,#1d1a2a,#5b4a5e 50%,#a68c7a)}
.brand{display:flex;align-items:center;gap:6px;font-family:"Montserrat",sans-serif;font-weight:700;color:var(--navy);letter-spacing:2px;text-transform:uppercase;white-space:nowrap}
.brand .dot{border-radius:50%;background:var(--navy);flex:none}
.brand.w{color:var(--white)}
.brand.w .dot{background:var(--white)}
.ring{position:absolute;border-radius:50%;border:10px solid var(--grey)}
.foot{position:absolute;left:10px;bottom:6px;width:6px;height:6px;border-radius:50%;background:var(--navy)}
.box{position:absolute;background:var(--navy);border-radius:6px;padding:6px}
.gbox{position:absolute;background:var(--grey);border-radius:6px;padding:6px}
.num{font-family:"Montserrat",sans-serif;font-weight:800;color:var(--navy);font-size:20px;line-height:1}
table{border-collapse:collapse;width:100%;font-size:6px}
th{background:var(--navy);color:#fff;font-family:"Montserrat",sans-serif;font-weight:600;padding:4px;text-align:left}
td{padding:4px;border-bottom:1px solid var(--grey);color:var(--text)}
.list li{list-style:none;font-size:6px;line-height:1.5;margin-bottom:5px;padding-left:8px;position:relative}
.list li::before{content:"";position:absolute;left:0;top:3px;width:4px;height:4px;border-radius:50%;background:var(--navy)}
.price{color:#fff;font-family:"Montserrat",sans-serif;font-weight:800;font-size:16px;padding:8px;text-align:center}
</style>
</head>
<body>
<main class="deck">

<section class="slide">
  <div class="photo ph-night" style="inset:0" role="img" aria-label="Evening city skyline in deep blue tones"></div>
  <div class="abs brand w" style="left:20px;top:96px;font-size:14px"><span class="dot" style="width:10px;height:10px"></span>Velvet Crane</div>
  <div class="abs" style="right:0;top:0;width:150px;height:212px;background:rgba(38,41,127,.85);padding:20px 14px">
    <div class="h w">Pictures, Text</div>
    <p class="p w" style="margin-top:8px">Share the story behind each gathering, the music that played and the glasses raised together.</p>
  </div>
</section>
<section class="slide">
  <div class="ring" style="left:-20px;top:20px;width:190px;height:190px"></div>
  <div class="photo ph-grey" style="left:190px;top:0;width:198px;height:120px" role="img" aria-label="Guests at a lively evening event"></div>
  <div class="abs" style="left:200px;top:132px;width:170px">
    <div class="h">Pictures, Text</div>
    <p class="p" style="margin-top:6px">Moments in time with the people we love, set to music, food and drink.</p>
  </div>
</section>
<section class="slide">
  <div class="photo ph-warm" style="left:30px;top:26px;width:140px;height:140px;border-radius:50%" role="img" aria-label="Warm toned photo of a party table"></div>
  <div class="abs brand" style="left:30px;width:140px;top:180px;justify-content:center;font-size:9px">Velvet Crane</div>
  <div class="abs" style="left:200px;top:90px;width:170px">
    <div class="h">Pictures, Text</div>
    <p class="p" style="margin-top:6px">A short description of the picture shown on this slide goes here.</p>
  </div>
</section>

<section class="slide">
  <div class="ring" style="left:134px;top:20px;width:120px;height:120px"></div>
  <div class="abs brand" style="left:0;right:0;top:156px;justify-content:center;font-size:12px;letter-spacing:5px;color:var(--mid)">Velvet Crane</div>
</section>
<section class="slide">
  <div class="abs brand" style="left:24px;top:98px;font-size:13px"><span class="dot" style="width:9px;height:9px"></span>Velvet Crane</div>
  <div class="abs" style="left:180px;top:86px;width:1px;height:40px;background:var(--mid)"></div>
  <div class="abs h" style="left:194px;top:100px;font-size:11px;letter-spacing:1px">YOUR SLIDES DECK NAME</div>
</section>
<section class="slide dark">
  <div class="abs brand w" style="left:24px;top:98px;font-size:13px"><span class="dot" style="width:9px;height:9px"></span>Velvet Crane</div>
  <div class="abs h w" style="left:194px;top:100px;font-size:11px;letter-spacing:1px">YOUR SLIDES DECK NAME</div>
</section>

<section class="slide">
  <div class="abs" style="left:14px;top:16px;width:80px">
    <div class="h">Pictures, Text</div>
    <p class="p" style="margin-top:6px">Add a brief summary for this picture and the moment it captures.</p>
  </div>
  <div class="photo ph-grey" style="left:100px;top:0;width:288px;height:212px" role="img" aria-label="Event hall with guests"></div>
  <svg class="abs" style="left:100px;top:0" width="288" height="212"><polygon points="40,0 90,0 40,212 0,212" fill="#3a3fae" opacity=".85"/></svg>
  <div class="abs" style="left:100px;top:130px;width:288px;height:82px;background:var(--navy);padding:16px">
    <div class="h w" style="font-size:13px">Description here</div>
    <p class="p w" style="margin-top:4px">Short supporting line of text.</p>
  </div>
</section>
<section class="slide">
  <div class="abs" style="left:0;top:0;width:130px;height:212px;background:var(--grey)"></div>
  <div class="abs h" style="left:14px;top:16px">How Column Text</div>
  <p class="abs p" style="left:14px;top:40px;width:105px">Introduce the idea in a few words before the detail column.</p>
  <div class="abs" style="left:145px;top:40px;width:228px">
    <p class="p">Whiskey, wine and food bring people to the table, and music keeps them there. Each event is designed around the memories guests carry home.</p>
    <p class="p" style="margin-top:8px">Describe the offer, the venue and the experience for investors in this column.</p>
  </div>
</section>
<section class="slide">
  <div class="abs h" style="left:14px;top:16px">How Column Text</div>
  <p class="abs p" style="left:14px;top:40px;width:220px">Use this slide to explain a single topic in detail. Keep each paragraph short, clear and focused on the guest experience.</p>
  <p class="abs p" style="left:14px;top:90px;width:220px">Add a second paragraph with figures or key points that support the story.</p>
  <div class="abs brand" style="left:262px;top:92px;font-size:9px"><span class="dot" style="width:7px;height:7px"></span>Velvet Crane</div>
</section>

<section class="slide">
  <div class="photo ph-neon" style="left:0;top:0;width:150px;height:212px" role="img" aria-label="Neon sign glowing in a bar"></div>
  <div class="abs h w" style="left:14px;top:96px;font-size:16px">AGENDA</div>
  <ol class="abs" style="left:170px;top:22px;width:200px;list-style:none">
    <li class="p" style="border-bottom:1px solid var(--grey);padding:3px 0">01 &nbsp; Welcome and introduction</li>
    <li class="p" style="border-bottom:1px solid var(--grey);padding:3px 0">02 &nbsp; Our story</li>
    <li class="p" style="border-bottom:1px solid var(--grey);padding:3px 0">03 &nbsp; Liquor and cellars</li>
    <li class="p" style="border-bottom:1px solid var(--grey);padding:3px 0">04 &nbsp; Food and events</li>
    <li class="p" style="border-bottom:1px solid var(--grey);padding:3px 0">05 &nbsp; Music studio</li>
    <li class="p" style="border-bottom:1px solid var(--grey);padding:3px 0">06 &nbsp; Market and growth</li>
    <li class="p" style="border-bottom:1px solid var(--grey);padding:3px 0">07 &nbsp; Investment</li>
  </ol>
</section>
<section class="slide">
  <div class="photo ph-grey" style="left:0;top:0;width:388px;height:60px;opacity:.5" role="img" aria-label="Soft photo of a dining room"></div>
  <div class="abs h" style="left:14px;top:74px">About<br>Our Company</div>
  <ul class="abs list" style="left:110px;top:74px;width:120px">
    <li>Founded on shared moments</li><li>Craft whiskey and wine</li><li>Live music nights</li><li>Private events</li>
  </ul>
  <ul class="abs list" style="left:250px;top:74px;width:120px">
    <li>Tasting rooms</li><li>Curated menus</li><li>Studio sessions</li><li>Community focus</li>
  </ul>
</section>
<section class="slide">
  <div class="abs" style="left:0;top:0;width:110px;height:212px;background:var(--grey)"></div>
  <div class="abs h" style="left:14px;top:90px">All Our<br>Projects</div>
  <div class="abs" style="left:125px;top:40px;display:grid;grid-template-columns:repeat(2,120px);gap:20px 10px">
    <div class="p"><b style="color:var(--navy)">● Project name</b><br>Short line of detail</div>
    <div class="p"><b style="color:var(--navy)">● Project name</b><br>Short line of detail</div>
    <div class="p"><b style="color:var(--navy)">● Project name</b><br>Short line of detail</div>
    <div class="p"><b style="color:var(--navy)">● Project name</b><br>Short line of detail</div>
    <div class="p"><b style="color:var(--navy)">● Project name</b><br>Short line of detail</div>
    <div class="p"><b style="color:var(--navy)">● Project name</b><br>Short line of detail</div>
  </div>
</section>

<section class="slide">
  <svg class="abs" style="left:40px;top:84px" width="28" height="28" viewBox="0 0 28 28"><rect x="2" y="2" width="24" height="24" rx="4" fill="none" stroke="#26297f" stroke-width="2.5"/><path d="M8 14l5 5 8-10" fill="none" stroke="#26297f" stroke-width="3"/></svg>
  <div class="abs h" style="left:40px;top:120px;font-size:9px">Section break</div>
  <div class="foot"></div>
</section>
<section class="slide">
  <div class="abs h" style="left:14px;top:40px">About<br>Our Company</div>
  <p class="abs p" style="left:14px;top:76px;width:150px">We craft spaces where drink, food and music come together for the moments people remember.</p>
  <div class="box" style="left:200px;top:40px;width:170px;height:26px"><span class="p w">Premium spirits</span></div>
  <div class="box" style="left:200px;top:72px;width:82px;height:40px"><span class="p w">Fine wine</span></div>
  <div class="box" style="left:288px;top:72px;width:82px;height:40px"><span class="p w">Live music</span></div>
  <div class="box" style="left:200px;top:118px;width:170px;height:26px"><span class="p w">Private events</span></div>
</section>
<section class="slide">
  <div class="abs" style="left:30px;top:46px;width:120px;height:120px;border-radius:50%;background:var(--navy);display:flex;align-items:center;justify-content:center;font-family:Montserrat,sans-serif;font-weight:800;font-size:28px;color:#fff">$5.3</div>
  <div class="abs" style="left:180px;top:50px;width:190px">
    <div class="p"><b style="color:var(--navy)">Milestone 01</b> First tasting room opens</div>
    <div style="height:1px;background:var(--grey);margin:10px 0"></div>
    <div class="p"><b style="color:var(--navy)">Milestone 02</b> Studio stage launched</div>
    <div style="height:1px;background:var(--grey);margin:10px 0"></div>
    <div class="p"><b style="color:var(--navy)">Milestone 03</b> Events across three cities</div>
  </div>
</section>

<section class="slide">
  <div class="abs h" style="left:14px;top:14px">Pictures, Text</div>
  <div class="box" style="left:14px;top:40px;width:170px;height:70px"><b class="p w">Add Text</b><p class="p w">Brief line about this point.</p></div>
  <div class="gbox" style="left:204px;top:40px;width:170px;height:70px"><b class="p">Add Text</b><p class="p">Brief line about this point.</p></div>
  <div class="gbox" style="left:14px;top:122px;width:170px;height:70px"><b class="p">Add Text</b><p class="p">Brief line about this point.</p></div>
  <div class="box" style="left:204px;top:122px;width:170px;height:70px"><b class="p w">Add Text</b><p class="p w">Brief line about this point.</p></div>
</section>
<section class="slide">
  <div class="abs h" style="left:14px;top:100px">Our Competitors</div>
  <div class="abs" style="left:140px;top:40px;display:grid;grid-template-columns:70px 70px 24px;gap:10px">
    <div style="height:24px;background:var(--grey);border-radius:3px"></div><div style="height:24px;background:var(--grey);border-radius:3px"></div><div style="height:24px;background:var(--blue);border-radius:50%"></div>
    <div style="height:24px;background:var(--grey);border-radius:3px"></div><div style="height:24px;background:var(--grey);border-radius:3px"></div><div style="height:24px;background:var(--blue);border-radius:50%"></div>
    <div style="height:24px;background:var(--grey);border-radius:3px"></div><div style="height:24px;background:var(--grey);border-radius:3px"></div><div style="height:24px;background:var(--blue);border-radius:50%"></div>
    <div style="height:24px;background:var(--grey);border-radius:3px"></div><div style="height:24px;background:var(--grey);border-radius:3px"></div><div style="height:24px;background:var(--blue);border-radius:50%"></div>
  </div>
</section>
<section class="slide">
  <div class="abs h" style="left:14px;top:14px">Pictures, Text</div>
  <div class="abs" style="left:20px;top:50px;display:grid;grid-template-columns:repeat(2,170px);gap:24px 10px">
    <div style="display:flex;gap:8px"><span class="num">01</span><p class="p"><b>Text Here</b><br>Short supporting line.</p></div>
    <div style="display:flex;gap:8px"><span class="num">02</span><p class="p"><b>Text Here</b><br>Short supporting line.</p></div>
    <div style="display:flex;gap:8px"><span class="num">03</span><p class="p"><b>Text Here</b><br>Short supporting line.</p></div>
    <div style="display:flex;gap:8px"><span class="num">04</span><p class="p"><b>Text Here</b><br>Short supporting line.</p></div>
  </div>
</section>

<section class="slide">
  <div class="abs brand" style="left:10px;top:64px;font-size:8px;letter-spacing:1px;color:var(--mid)">Velvet Crane</div>
  <div class="abs" style="left:110px;top:20px;width:110px;height:172px;background:var(--navy);padding:14px">
    <div class="h w">Company Statistics</div>
    <p class="p w" style="margin-top:8px">Key numbers that show growth across venues and events.</p>
  </div>
  <div class="photo ph-warm" style="left:220px;top:20px;width:154px;height:172px" role="img" aria-label="Row of whiskey glasses on a bar"></div>
</section>
<section class="slide">
  <div class="ring" style="left:20px;top:16px;width:180px;height:180px"></div>
  <div class="abs" style="left:70px;top:66px;width:80px;height:80px;border-radius:50%;background:var(--navy);display:flex;align-items:center;justify-content:center;text-align:center"><span class="h w" style="font-size:8px">Our<br>Company</span></div>
  <p class="abs p" style="left:220px;top:92px;width:150px">Tell investors who we are, what we stand for and where we are heading next.</p>
</section>
<section class="slide">
  <div class="abs h" style="left:14px;top:14px">Pictures, Text</div>
  <div class="photo ph-grey" style="left:14px;top:44px;width:110px;height:90px;border-radius:8px" role="img" aria-label="Image placeholder"></div>
  <div class="photo ph-grey" style="left:139px;top:44px;width:110px;height:90px;border-radius:8px" role="img" aria-label="Image placeholder"></div>
  <div class="photo ph-grey" style="left:264px;top:44px;width:110px;height:90px;border-radius:8px" role="img" aria-label="Image placeholder"></div>
  <p class="abs p" style="left:14px;top:144px;width:110px">Caption text here.</p>
  <p class="abs p" style="left:139px;top:144px;width:110px">Caption text here.</p>
  <p class="abs p" style="left:264px;top:144px;width:110px">Caption text here.</p>
</section>

<section class="slide">
  <div class="abs" style="left:0;top:0;width:388px;height:70px;background:var(--navy)"></div>
  <div class="abs h w" style="left:14px;top:30px;font-size:13px">Our Services</div>
  <p class="abs p" style="left:14px;top:90px;width:170px">Tastings, dinners, concerts and private celebrations, all planned around the people in the room.</p>
  <div class="photo ph-bar" style="left:200px;top:40px;width:170px;height:150px" role="img" aria-label="Microphone on a stage under warm light"></div>
</section>
<section class="slide">
  <div class="photo ph-night" style="inset:0" role="img" aria-label="Crowd at a concert with stage lights"></div>
  <div class="abs" style="left:150px;top:0;width:238px;height:212px;background:rgba(38,41,127,.9);padding:30px 18px">
    <p class="p w" style="margin-bottom:12px"><b>● Service one</b> short description</p>
    <p class="p w" style="margin-bottom:12px"><b>● Service two</b> short description</p>
    <p class="p w" style="margin-bottom:12px"><b>● Service three</b> short description</p>
    <p class="p w"><b>● Service four</b> short description</p>
  </div>
</section>
<section class="slide">
  <div class="abs" style="left:0;top:0;width:388px;height:80px;background:var(--navy)"></div>
  <div class="abs h w" style="left:14px;top:30px;font-size:13px">Our History</div>
  <div class="photo ph-grey" style="left:40px;top:66px;width:60px;height:60px;border-radius:50%;border:3px solid #fff" role="img" aria-label="Early venue photo"></div>
  <div class="photo ph-grey" style="left:164px;top:66px;width:60px;height:60px;border-radius:50%;border:3px solid #fff" role="img" aria-label="Studio opening photo"></div>
  <div class="photo ph-grey" style="left:288px;top:66px;width:60px;height:60px;border-radius:50%;border:3px solid #fff" role="img" aria-label="Recent event photo"></div>
  <p class="abs p" style="left:24px;top:140px;width:92px;text-align:center">2015 first cellar</p>
  <p class="abs p" style="left:148px;top:140px;width:92px;text-align:center">2018 studio stage</p>
  <p class="abs p" style="left:272px;top:140px;width:92px;text-align:center">2023 new venues</p>
</section>

<section class="slide">
  <div class="abs h" style="left:14px;top:14px">Your Title Goes Here</div>
  <div class="abs num" style="left:14px;top:40px;font-size:24px">250K</div>
  <div class="abs" style="left:14px;top:84px;width:180px">
    <div style="height:6px;width:90%;background:var(--navy);margin-bottom:8px"></div>
    <div style="height:6px;width:70%;background:var(--blue);margin-bottom:8px"></div>
    <div style="height:6px;width:55%;background:var(--mid);margin-bottom:8px"></div>
    <div style="height:6px;width:40%;background:var(--grey)"></div>
  </div>
  <svg class="abs" style="left:230px;top:50px" width="130" height="110" viewBox="0 0 130 110"><ellipse cx="65" cy="60" rx="60" ry="40" fill="#b9bacb"/><path d="M65 60 L65 20 A60 40 0 1 1 10 75 Z" fill="#3a3fae"/><path d="M65 60 L10 75 A60 40 0 0 1 65 20 Z" fill="#26297f"/></svg>
</section>
<section class="slide">
  <div class="abs h" style="left:14px;top:14px">Your Title Goes Here</div>
  <svg class="abs" style="left:124px;top:40px" width="140" height="140" viewBox="0 0 140 140">
    <circle cx="70" cy="70" r="46" fill="none" stroke="#e7e7ee" stroke-width="3"/>
    <circle cx="70" cy="24" r="12" fill="#26297f"/><circle cx="110" cy="47" r="12" fill="#3a3fae"/><circle cx="110" cy="93" r="12" fill="#26297f"/>
    <circle cx="70" cy="116" r="12" fill="#3a3fae"/><circle cx="30" cy="93" r="12" fill="#26297f"/><circle cx="30" cy="47" r="12" fill="#3a3fae"/>
  </svg>
  <p class="abs p" style="left:14px;top:70px;width:100px">Step text here with a short line.</p>
  <p class="abs p" style="left:280px;top:70px;width:100px">Step text here with a short line.</p>
  <p class="abs p" style="left:14px;top:130px;width:100px">Step text here with a short line.</p>
  <p class="abs p" style="left:280px;top:130px;width:100px">Step text here with a short line.</p>
</section>
<section class="slide">
  <div class="abs h" style="left:14px;top:14px">One Column Text</div>
  <p class="abs p" style="left:14px;top:40px;width:360px">Every great evening starts with a pour and ends with a song. Our venues bring craft whiskey, fine wine and shared plates together with live music, creating a setting where guests slow down and enjoy the company around them.</p>
  <p class="abs p" style="left:14px;top:90px;width:360px">Use this column for a longer explanation of the business model, the guest journey or the plan for growth. Keep the tone warm and the facts clear so investors can follow the story from the first glass to the last note.</p>
  <div class="foot"></div>
</section>

<section class="slide">
  <div class="abs" style="left:0;top:0;width:8px;height:212px;background:var(--navy)"></div>
  <div class="abs h" style="left:20px;top:20px">Bulleted List<br>Text Sample</div>
  <ul class="abs list" style="left:20px;top:60px;width:110px"><li>First point</li><li>Second point</li><li>Third point</li></ul>
  <div class="photo ph-bar" style="left:140px;top:20px;width:130px;height:172px" role="img" aria-label="Dinner party table with candles"></div>
  <div class="abs" style="left:270px;top:50px;width:104px;height:110px;background:var(--navy);padding:10px"><p class="p w">Short highlight text for the picture beside it.</p></div>
</section>
<section class="slide">
  <div class="abs h" style="left:14px;top:14px">Your Title Goes Here</div>
  <svg class="abs" style="left:14px;top:40px" width="360" height="26" viewBox="0 0 360 26"><polygon points="0,0 110,0 122,13 110,26 0,26" fill="#26297f"/><polygon points="120,0 230,0 242,13 230,26 120,26 132,13" fill="#3a3fae"/><polygon points="240,0 360,0 360,26 240,26 252,13" fill="#26297f"/></svg>
  <p class="abs p" style="left:14px;top:80px;width:108px">Phase one text with a short description.</p>
  <p class="abs p" style="left:134px;top:80px;width:108px">Phase two text with a short description.</p>
  <p class="abs p" style="left:254px;top:80px;width:108px">Phase three text with a short description.</p>
</section>
<section class="slide">
  <div class="abs h" style="left:14px;top:14px">Two Column Text</div>
  <p class="abs p" style="left:14px;top:40px;width:170px">Left column text describing the first half of the idea, with enough detail for a reader to follow along.</p>
  <p class="abs p" style="left:204px;top:40px;width:170px">Right column text describing the second half of the idea and closing the point clearly.</p>
</section>

<section class="slide">
  <div class="abs h" style="left:14px;top:30px">Our Target</div>
  <p class="abs p" style="left:14px;top:54px;width:130px">The guests and partners we are building for.</p>
  <div class="box" style="left:170px;top:30px;width:200px;height:60px"><p class="p w"><b>Audience one</b><br>Adults who love great nights out.</p></div>
  <div class="box" style="left:170px;top:100px;width:200px;height:60px"><p class="p w"><b>Audience two</b><br>Hosts planning private events.</p></div>
</section>
<section class="slide">
  <div class="photo ph-bar" style="left:0;top:0;width:180px;height:104px" role="img" aria-label="Bar counter with bottles"></div>
  <div class="photo ph-night" style="left:0;top:108px;width:180px;height:104px" role="img" aria-label="Band playing to a crowd"></div>
  <div class="abs" style="left:180px;top:0;width:208px;height:104px;background:var(--navy);padding:16px"><div class="h w">Text Information Here</div><p class="p w" style="margin-top:4px">Short description of this area.</p></div>
  <div class="abs" style="left:180px;top:108px;width:208px;height:104px;padding:16px"><div class="h">Text Information Here</div><p class="p" style="margin-top:4px">Short description of this area.</p></div>
</section>
<section class="slide">
  <div class="abs h" style="left:14px;top:14px">Bulleted List Text Sample</div>
  <ul class="abs list" style="left:14px;top:40px;width:360px">
    <li><b>Text Headline</b> Supporting text for the first point.</li>
    <li><b>Text Headline</b> Supporting text for the second point.</li>
    <li><b>Text Headline</b> Supporting text for the third point.</li>
    <li><b>Text Headline</b> Supporting text for the fourth point.</li>
    <li><b>Text Headline</b> Supporting text for the fifth point.</li>
  </ul>
</section>

<section class="slide">
  <div class="abs h" style="left:14px;top:14px">Table</div>
  <div class="abs" style="left:14px;top:38px;width:360px">
    <table><tr><th>Item</th><th>Q1</th><th>Q2</th><th>Q3</th><th>Q4</th></tr>
    <tr><td>Spirits</td><td>120</td><td>140</td><td>155</td><td>170</td></tr>
    <tr><td>Wine</td><td>90</td><td>98</td><td>110</td><td>125</td></tr>
    <tr><td>Food</td><td>60</td><td>72</td><td>80</td><td>95</td></tr>
    <tr><td>Music</td><td>40</td><td>55</td><td>62</td><td>70</td></tr>
    <tr><td>Events</td><td>30</td><td>44</td><td>58</td><td>66</td></tr></table>
  </div>
</section>
<section class="slide">
  <div class="abs h" style="left:14px;top:14px">Table II</div>
  <div class="abs" style="left:14px;top:38px;width:360px">
    <table><tr><th>Venue</th><th>Seats</th><th>Events</th><th>Rating</th></tr>
    <tr><td>Cellar room</td><td>80</td><td>24</td><td>4.8</td></tr>
    <tr><td>Studio stage</td><td>150</td><td>36</td><td>4.7</td></tr>
    <tr><td>Garden bar</td><td>120</td><td>18</td><td>4.6</td></tr>
    <tr><td>Tasting hall</td><td>60</td><td>30</td><td>4.9</td></tr>
    <tr><td>Rooftop</td><td>100</td><td>22</td><td>4.5</td></tr></table>
  </div>
</section>
<section class="slide">
  <div class="abs h" style="left:14px;top:14px">Prices</div>
  <div class="abs" style="left:14px;top:40px;width:112px;height:150px;background:var(--grey)"><div class="price" style="background:var(--mid)">20$</div><p class="p" style="padding:8px">Tasting pass<br>Two pours<br>Small plate</p></div>
  <div class="abs" style="left:138px;top:34px;width:112px;height:162px;background:var(--navy)"><div class="price" style="background:var(--blue)">30$</div><p class="p w" style="padding:8px">Evening pass<br>Four pours<br>Live set</p></div>
  <div class="abs" style="left:262px;top:40px;width:112px;height:150px;background:var(--grey)"><div class="price" style="background:var(--mid)">50$</div><p class="p" style="padding:8px">Full night<br>Dinner<br>Studio tour</p></div>
</section>

<section class="slide">
  <div class="ring" style="left:124px;top:16px;width:140px;height:140px;opacity:.7"></div>
  <div class="abs h" style="left:0;right:0;top:78px;text-align:center;font-size:14px">Get in Touch</div>
  <svg class="abs" style="left:120px;top:170px" width="150" height="20" viewBox="0 0 150 20">
    <circle cx="15" cy="10" r="9" fill="#26297f"/><path d="M11 6l2 0 1 3-1 1a6 6 0 0 0 3 3l1-1 3 1 0 2a2 2 0 0 1-2 1A10 10 0 0 1 10 8a2 2 0 0 1 1-2z" fill="#fff"/>
    <circle cx="75" cy="10" r="9" fill="#26297f"/><rect x="70" y="7" width="10" height="7" fill="none" stroke="#fff"/><path d="M70 7l5 4 5-4" fill="none" stroke="#fff"/>
    <circle cx="135" cy="10" r="9" fill="#26297f"/><path d="M135 15s-4-4-4-7a4 4 0 0 1 8 0c0 3-4 7-4 7z" fill="#fff"/>
  </svg>
</section>
<section class="slide">
  <div class="abs brand" style="left:0;right:0;top:96px;justify-content:center;font-size:18px"><span class="dot" style="width:12px;height:12px"></span>Velvet Crane</div>
</section>
<section class="slide">
  <div class="abs brand" style="left:0;right:0;top:70px;justify-content:center;font-size:14px"><span class="dot" style="width:10px;height:10px"></span>Velvet Crane</div>
  <div class="abs brand" style="left:0;right:0;top:122px;justify-content:center;font-size:14px;color:var(--blue)"><span class="dot" style="width:10px;height:10px;background:var(--blue)"></span>Velvet Crane</div>
</section>

</main>
</body>
</html>
```